Business Card

We need some ideas for corporate business cards. I'm interested in a double sided card, with one side featuring our corporate logo, the other side with employee information.

Corporate colors, logo etc. available at www.varnik.com

Industry/Entity Type

Business

Requirements
Must have
• The "Varnik" logo with stylized "O"

Nice to have
• Preferred font is calibri

```html
<!DOCTYPE html>
<html lang="en">
<head>
<meta charset="utf-8">
<title>Varnik Business Cards</title>
<link rel="stylesheet" href="https://fonts.googleapis.com/css2?family=Carlito:ital,wght@0,400;0,700;1,400;1,700&display=swap">
<style>
  :root {
    --page-bg: #efe9df;
    --maroon: #9c3350;
    --slate: #52689a;
    --paper: #ffffff;
    --ink-dark: #1c1c1c;
    --ink-blue: #4a5f93;
    --svc-sb: #e5892b;
    --svc-ud: #5b82b8;
    --svc-rc: #8f1f45;
    --svc-ag: #17706e;
  }
  * { box-sizing: border-box; margin: 0; padding: 0; }
  html, body { width: 1200px; height: 1000px; overflow: hidden; }
  body {
    background: var(--page-bg);
    font-family: "Carlito", "Calibri", sans-serif;
    position: relative;
  }
  .card {
    position: absolute;
    width: 580px;
    height: 330px;
    box-shadow: 0 8px 22px rgba(0,0,0,.22);
    overflow: hidden;
  }
  .theme-maroon { --brand: var(--maroon); --name-ink: var(--ink-blue); --label-ink: var(--ink-blue); }
  .theme-slate  { --brand: var(--slate);  --name-ink: var(--ink-dark); --label-ink: var(--ink-dark); }

  /* Front side */
  .card-front { background: var(--paper); }
  .card-front .top-band {
    position: absolute; left: 0; top: 0; width: 100%; height: 70px;
    background: var(--brand);
    display: flex; align-items: center; justify-content: center;
  }
  .wordmark {
    color: var(--paper);
    font-weight: 700;
    letter-spacing: 6px;
    line-height: 1;
  }
  .top-band .wordmark { font-size: 50px; }
  .card-front .bottom-band {
    position: absolute; left: 0; bottom: 0; width: 100%; height: 50px;
    background: var(--brand);
    color: var(--paper);
    font-style: italic; font-size: 13px; line-height: 1.3;
    text-align: center;
    padding: 8px 110px 0;
  }
  .person {
    position: absolute; left: 0; width: 100%; top: 92px; text-align: center;
    line-height: 1.2;
  }
  .person-name { font-size: 22px; color: var(--name-ink); }
  .person-title { font-size: 19px; font-weight: 700; font-style: italic; color: var(--maroon); }
  .contacts {
    position: absolute; left: 30px; top: 142px;
    font-size: 14px; line-height: 1.35; color: var(--label-ink);
  }
  .section-head { font-size: 16px; font-weight: 700; color: var(--maroon); }
  .contacts b { font-weight: 700; }
  .services {
    position: absolute; left: 410px; top: 168px;
    font-size: 14px; line-height: 1.35; color: var(--ink-blue);
  }
  .theme-slate .services { color: var(--ink-dark); }
  .service { display: flex; align-items: center; gap: 5px; }
  .svc-badge {
    width: 15px; height: 15px; font-size: 7px; font-weight: 700;
    color: var(--paper); display: inline-flex; align-items: center; justify-content: center;
  }
  .svc-sb { background: var(--svc-sb); }
  .svc-ud { background: var(--svc-ud); }
  .svc-rc { background: var(--svc-rc); }
  .svc-ag { background: var(--svc-ag); }

  /* Back side */
  .card-back {
    background: var(--brand);
    display: flex; align-items: center; justify-content: center;
  }
  .card-back .wordmark { font-size: 84px; letter-spacing: 10px; }

  .pos-front-top { left: 40px;  top: 80px; }
  .pos-back-top  { left: 640px; top: 120px; width: 520px; }
  .pos-front-bot { left: 40px;  top: 570px; }
  .pos-back-bot  { left: 640px; top: 580px; width: 520px; }
</style>
</head>
<body>

<section class="card card-front theme-maroon pos-front-top">
  <div class="top-band"><span class="wordmark">VARNIK</span></div>
  <div class="person">
    <p class="person-name">M.r Calloway</p>
    <p class="person-title">Marketing Manager</p>
  </div>
  <div class="contacts">
    <p class="section-head">CONTACTS:</p>
    <p><b>Phone:</b> +1 42-5310 78</p>
    <p><b>Mobile:</b> +431902 6</p>
    <p><b>Email:</b> calloway@varnik.com</p>
    <p><b>FB:</b> Varnik</p>
    <p><b>Box:</b> 41 26, Marlow strt, Fairport City.</p>
  </div>
  <div class="services">
    <p class="section-head">SERVICES:</p>
    <p class="service"><span class="svc-badge svc-sb">SB</span>Smart billing</p>
    <p class="service"><span class="svc-badge svc-ud">UD</span>Unified Data Flow</p>
    <p class="service"><span class="svc-badge svc-rc">RC</span>Rate control</p>
    <p class="service"><span class="svc-badge svc-ag">AG</span>Access Gateway</p>
  </div>
  <p class="bottom-band">Varnik technology brings clarity, command, revenue and connection to the world's leading network carriers</p>
</section>

<section class="card card-back theme-maroon pos-back-top">
  <span class="wordmark">VARNIK</span>
</section>

<section class="card card-front theme-slate pos-front-bot">
  <div class="top-band"><span class="wordmark">VARNIK</span></div>
  <div class="person">
    <p class="person-name">M.r Calloway</p>
    <p class="person-title">Marketing Manager</p>
  </div>
  <div class="contacts">
    <p class="section-head">CONTACTS:</p>
    <p><b>Phone:</b> +1 42-5310 78</p>
    <p><b>Mobile:</b> +431902 6</p>
    <p><b>Email:</b> calloway@varnik.com</p>
    <p><b>FB:</b> Varnik</p>
    <p><b>Box:</b> 41 26, Marlow strt, Fairport City.</p>
  </div>
  <div class="services">
    <p class="section-head">SERVICES:</p>
    <p class="service"><span class="svc-badge svc-sb">SB</span>Smart billing</p>
    <p class="service"><span class="svc-badge svc-ud">UD</span>Unified Data Flow</p>
    <p class="service"><span class="svc-badge svc-rc">RC</span>Rate control</p>
    <p class="service"><span class="svc-badge svc-ag">AG</span>Access Gateway</p>
  </div>
  <p class="bottom-band">Varnik technology brings clarity, command, revenue and connection to the world's leading network carriers</p>
</section>

<section class="card card-back theme-slate pos-back-bot">
  <span class="wordmark">VARNIK</span>
</section>

</body>
</html>
```